VKL MT Academy

Cosmetic dentistry Utilizing the latest smile simulation technology (VKL )to show patients their after smile results and allow them to be involved in the design prior to treatment
Please review the following websites to understand the concept:

http://www.clipvault.example/watch?v=Qm7RtLwZpAe
http://www.clipvault.example/watch?v=Hu3KsNvBxYc

www.vklportal.example.au

www.malcolmtennant.example.au
Dr Malcolm Tennant the Clinical director of the MT Academy is the leading cosmetic dentist in Australia and runs the Institute that teaches dentists how to deliver their cosmetic results
he also owns the Australian rites to VKL
Updates

It may be necessary to do 2 versions for the cards

One for the female market that basically trends of the Clipvault site i sent that "sex sells" and youthful smiles are more attractive for the aging woman who has the $$ to spend on a Smile makeover

A second card that is for the male senior manager exec who has not looked after their teeth due to work commitments but does not want the Smile Makeover look yet they need to compete with the younger execs snapping at their heels and if they are in the media they want to have an improved smile

The Simulation process we have developed allows them to see the end result before they commit
Their greatest fear is the obvious smile change and the CHICLET SMILE look

Target Market(s)

25-45 year olds, first group the professional male, second group females who want to improve their smile but be able to control the result

Industry/Entity Type

Clipvault

Contact Information for Business Card

Virtual Kinetic Layout
The MT Academy

Requirements
Must have
• The VKL logo on front with the MT Academy
Nice to have
• background picture of beautiful smile right hand side with copy over it
VKL logo left hand side

```html
<!DOCTYPE html>
<html lang="en">
<head>
<meta charset="utf-8">
<title>VKL MT Academy – Business Card</title>
<link href="https://fonts.googleapis.com/css2?family=Open+Sans:wght@400;600;700&display=swap" rel="stylesheet">
<style>
  :root {
    --canvas: #ffffff;
    --card-dark: #050505;
    --card-light: #ffffff;
    --accent-red: #e8392b;
    --text-light: #ffffff;
    --text-dark: #111111;
    --rule: #222222;
    --mark-grey: #8a8a8a;
    --card-edge: #d6d6d6;
    --skin-warm: #b8743f;
    --skin-deep: #6a3a1a;
  }
  * { box-sizing: border-box; margin: 0; padding: 0; }
  html, body {
    width: 1200px; height: 900px; overflow: hidden;
    background: var(--canvas);
    font-family: "Open Sans", Arial, sans-serif;
  }
  .stage { position: relative; width: 1200px; height: 900px; }

  .card {
    position: absolute;
    width: 580px; height: 340px;
    border-radius: 14px;
    overflow: hidden;
  }

  /* Brand lock-up */
  .brand { position: absolute; display: flex; flex-direction: column; }
  .brand__row {
    display: flex; align-items: center; gap: 10px;
    font-weight: 400; color: var(--accent-red); line-height: 1;
  }
  .brand__dot { border-radius: 50%; border: 2px solid var(--mark-grey); flex: none; }
  .brand__tagline { color: var(--mark-grey); font-weight: 400; white-space: nowrap; }

  /* Front card */
  .card--front {
    left: 480px; top: 70px;
    background: var(--card-dark);
    color: var(--text-light);
  }
  .card--front .brand { left: 28px; top: 196px; }
  .card--front .brand__row { font-size: 50px; letter-spacing: 3px; }
  .card--front .brand__dot { width: 22px; height: 22px; }
  .card--front .brand__tagline { font-size: 10.5px; margin-top: 6px; }

  .contact {
    position: absolute; left: 196px; top: 96px;
    width: 214px; text-align: center; white-space: nowrap;
  }
  .contact__name { color: var(--accent-red); font-weight: 700; font-size: 16px; }
  .contact__role { font-size: 12px; margin-top: 2px; }
  .contact__lines { list-style: none; margin-top: 18px; font-size: 12.5px; line-height: 19px; }

  .portrait { position: absolute; }
  .card--front .portrait {
    right: 0; top: 70px; width: 168px; height: 220px;
    background: radial-gradient(ellipse at 50% 45%, var(--skin-warm) 0%, var(--skin-deep) 45%, var(--card-dark) 75%);
  }
  .address {
    position: absolute; left: 0; right: 0; bottom: 22px;
    text-align: center; white-space: nowrap;
    color: var(--accent-red); font-weight: 700; font-size: 14px;
  }

  /* Back card */
  .card--back {
    left: 140px; top: 470px;
    background: var(--card-light);
    border: 1px solid var(--card-edge);
    color: var(--text-dark);
  }
  .appointments { position: absolute; left: 34px; top: 46px; width: 310px; }
  .appointments__title { font-weight: 700; font-size: 16px; }
  .appointments__line { height: 31px; border-bottom: 1px solid var(--rule); }
  .card--back .brand { left: 36px; bottom: 26px; }
  .card--back .brand__row { font-size: 36px; letter-spacing: 3px; }
  .card--back .brand__dot { width: 16px; height: 16px; }
  .card--back .brand__tagline { font-size: 9px; margin-top: 4px; }
  .card--back .portrait {
    bottom: 20px; right: 6px; width: 220px; height: 280px;
    background: radial-gradient(ellipse at 50% 40%, var(--skin-warm) 0%, #d7a77d 40%, var(--card-light) 72%);
  }
</style>
</head>
<body>
<main class="stage">
  <section class="card card--front" aria-label="Business card front">
    <div class="brand">
      <div class="brand__row"><span class="brand__dot"></span>VKL</div>
      <p class="brand__tagline">Virtual Kinetic Layout · MT Academy</p>
    </div>
    <div class="contact">
      <p class="contact__name">Dr MALCOLM TENNANT</p>
      <p class="contact__role">Dentist</p>
      <ul class="contact__lines">
        <li>1800 555 214</li>
        <li>info@malcolmtennant.example.au</li>
        <li>www.vklportal.example.au</li>
        <li>www.malcolmtennant.example.au</li>
      </ul>
    </div>
    <div class="portrait" role="img" aria-label="Photo of a smiling woman resting her face on her hands"></div>
    <p class="address">LEVEL 2, 48 HARBOUR LANE SOUTHBANK 3006 AUSTRALIA</p>
  </section>

  <section class="card card--back" aria-label="Business card back">
    <div class="appointments">
      <p class="appointments__title">Appointments:</p>
      <div class="appointments__line"></div>
      <div class="appointments__line"></div>
      <div class="appointments__line"></div>
      <div class="appointments__line"></div>
      <div class="appointments__line"></div>
    </div>
    <div class="portrait" role="img" aria-label="Photo of a smiling woman resting her face on her hands"></div>
    <div class="brand">
      <div class="brand__row"><span class="brand__dot"></span>VKL</div>
      <p class="brand__tagline">Virtual Kinetic Layout · MT Academy</p>
    </div>
  </section>
</main>
</body>
</html>
```